Technology Charity needs a Web Design

Velmo Puna purchases used company mobiles and donates the proceeds to charity. It is showing companies how they can do social good, with unused technology. We would like to see designs with relevant images of social good. Open to ideas, and more is explained in the attached brief. Logo is attached as well.

```html
<!DOCTYPE html>
<html lang="en">
<head>
<meta charset="utf-8">
<title>Velmo Puna – Web Design Concepts</title>
<link href="https://fonts.googleapis.com/css2?family=Poppins:wght@300;400;500;600;700&display=swap" rel="stylesheet">
<style>
:root{
  --stage:#9b999a;
  --white:#ffffff;
  --ink:#2b2b2b;
  --muted:#7a7a7a;
  --olive:#c5c8a5;
  --olive-btn:#c4c6a0;
  --steel:#8eafb8;
  --steel-dark:#7fa3ad;
  --sage:#a5bcb0;
  --footer:#333333;
  --link:#7fa3ad;
}
*{box-sizing:border-box;margin:0;padding:0}
html,body{width:1200px;height:2187px;overflow:hidden}
body{background:var(--stage);font-family:'Poppins',sans-serif;color:var(--ink);position:relative}
.page{position:absolute;top:62px;width:530px;height:2062px;background:var(--white);overflow:hidden;box-shadow:0 2px 6px rgba(0,0,0,.25)}
.page--a{left:53px}
.page--b{left:617px}
section,header,footer{position:relative;width:530px}

/* header */
.site-header{height:38px;background:var(--white);border-top:2px solid var(--steel)}
.brand{position:absolute;left:64px;top:9px;display:flex;align-items:center;gap:6px;font-size:15px;font-weight:500;color:var(--steel-dark)}
.brand-mark{width:9px;height:9px;border-radius:50%;background:var(--olive)}
.nav{position:absolute;left:221px;top:15px;display:flex;gap:10px;font-size:6px;font-weight:500}
.nav .is-active{color:var(--steel-dark)}

/* hero */
.hero{height:282px}
.hero-photo{position:absolute;inset:0}
.page--a .hero-photo{background:linear-gradient(120deg,#1e3550 0%,#2f5d7c 35%,#5f8fae 55%,#2a4a66 80%),radial-gradient(circle at 5% 90%,#e08a2c,transparent 50%);background-blend-mode:screen}
.page--b .hero-photo{background:linear-gradient(180deg,#3d5a2c 0%,#6f8f5a 25%,#8fb4cc 55%,#7aa0bb 80%,#3e5570 100%)}
.hero-title{position:absolute;left:0;right:0;top:108px;text-align:center;color:var(--white);font-size:20.5px;font-weight:600;line-height:23px;text-shadow:0 1px 3px rgba(0,0,0,.5)}
.btn{display:inline-flex;align-items:center;gap:4px;background:var(--olive-btn);color:var(--white);font-size:6.5px;font-weight:500;padding:0 10px;height:22px;text-transform:uppercase}
.btn::after{content:"";width:6px;height:6px;border-radius:50%;background:var(--white)}
.hero .btn{position:absolute;left:227px;top:194px;height:21px}
.hero-dots{position:absolute;left:500px;top:112px;display:flex;flex-direction:column;gap:7px}
.hero-dots span{width:4px;height:4px;border-radius:50%;background:var(--white)}
.corner-tris{position:absolute;right:0;top:230px;z-index:2}

/* what we do */
.what{height:290px}
.hex{position:absolute;left:33px;top:36px}
.what h2{position:absolute;left:268px;top:36px;font-size:20px;font-weight:700}
.what p{position:absolute;left:268px;top:77px;width:200px;font-size:5.4px;line-height:13.8px;color:var(--muted)}
.what .btn{position:absolute;left:268px;top:218px}

/* benefits */
.benefits{height:444px;background:var(--olive)}
.section-title{position:absolute;left:0;right:0;text-align:center;font-weight:700}
.benefits .section-title{top:44px;font-size:21px}
.benefits .lead{position:absolute;left:0;right:0;top:90px;text-align:center;font-size:5.6px;line-height:13.5px;color:#6e705c}
.cards{position:absolute;left:65px;top:141px;display:grid;grid-template-columns:repeat(3,129px);gap:8px}
.card{height:122px;background:var(--white);text-align:center;padding-top:10px}
.card svg{display:block;margin:0 auto}
.card h3{font-size:7.2px;font-weight:500;line-height:10.5px;margin-top:8px}
.card p{font-size:5px;line-height:9.5px;color:var(--muted);margin-top:5px;padding:0 14px}
.card .more{display:block;font-size:6px;font-weight:600;color:var(--link);margin-top:8px}

/* how */
.how{height:378px;background:var(--steel)}
.how .section-title{top:34px;font-size:20px;color:var(--white)}
.how .lead{position:absolute;left:0;right:0;top:73px;text-align:center;font-size:5.6px;color:var(--white)}
.step{position:absolute;width:108px;height:108px;border-radius:50%;border:1.5px solid rgba(255,255,255,.45);color:var(--white);text-align:center}
.step b{position:absolute;left:0;right:0;font-size:17px;font-weight:600;color:rgba(255,255,255,.85)}
.step p{position:absolute;left:11px;right:11px;font-size:4.9px;line-height:9px}
.step--top b{top:12px}.step--top p{top:41px}
.step--bot b{bottom:10px}.step--bot p{top:18px}
.how-tris{position:absolute;left:0;bottom:0}

/* contact */
.contact{height:291px}
.contact h2{position:absolute;left:63px;top:36px;font-size:20px;font-weight:700}
.contact .lead{position:absolute;left:63px;top:71px;font-size:5.6px;color:var(--muted)}
.form{position:absolute;left:63px;top:97px;width:213px;display:grid;grid-template-columns:1fr 1fr;gap:7px 3px}
.field{height:23px;border:1px solid #bfbfbf;font-size:5.6px;color:#666;padding:0 11px;display:flex;align-items:center;justify-content:space-between}
.field--wide{grid-column:1/3}
.contact .btn{position:absolute;left:63px;top:229px}
.contact-photo{position:absolute;left:302px;top:0;width:228px;height:291px;background:linear-gradient(160deg,#7b6a5a 0%,#5b6b70 40%,#c9b79a 60%,#3c4a55 100%)}

/* mission */
.mission{height:246px;background:var(--sage)}
.mission-photo{position:absolute;inset:0}
.mission h2{position:absolute;left:63px;top:48px;font-size:20px;font-weight:700;color:var(--white)}
.mission p{position:absolute;left:63px;width:200px;font-size:6.4px;line-height:12.5px;color:var(--white)}
.mission .p1{top:76px}.mission .p2{top:131px}
.mission .btn{position:absolute;left:63px;top:201px}

/* footer */
.site-footer{height:93px;background:var(--footer);color:var(--white);text-align:center}
.social{position:absolute;left:0;right:0;top:20px;display:flex;justify-content:center;gap:3px}
.social span{width:12px;height:12px;border-radius:50%;border:1px solid var(--white)}
.foot-nav{position:absolute;left:0;right:0;top:46px;display:flex;justify-content:center;gap:12px;font-size:7px;font-weight:600}
.copy{position:absolute;left:0;right:0;top:68px;font-size:5.6px}
</style>
</head>
<body>

<!-- concept A -->
<div class="page page--a">
  <header class="site-header">
    <div class="brand"><span class="brand-mark"></span>Velmo Puna</div>
    <nav class="nav"><span class="is-active">What we do</span><span>Benefits</span><span>How Does It Work?</span><span>Contact Us</span><span>Our Mission</span></nav>
  </header>
  <section class="hero">
    <div class="hero-photo" role="img" aria-label="Business people silhouetted against glass office towers at sunset"></div>
    <h1 class="hero-title">Velmo Puna helping organisations<br>give to meaningful causes<br>through used technology</h1>
    <span class="btn">Get Started</span>
    <div class="hero-dots"><span></span><span></span><span></span><span></span></div>
    <svg class="corner-tris" width="90" height="70" viewBox="0 0 90 70"><polygon points="30,0 60,52 0,52" fill="#c5c8a5"/><polygon points="62,10 90,66 26,66" fill="#8eafb8"/></svg>
  </section>
  <section class="what">
    <svg class="hex" width="220" height="198" viewBox="0 0 220 198"><polygon points="55,2 165,2 218,99 165,196 55,196 2,99" fill="#fff" stroke="#cfcfcf"/><polygon points="60,6 160,6 210,99 160,192 60,192 10,99" fill="#7d9cb8" role="img" aria-label="Smiling man in glasses and a denim shirt looking at his phone"/></svg>
    <h2>What We Do</h2>
    <p>Velmo Puna creates an easy pathway for organisations, to become more sustainable, renewable and give back to the community. We do this by purchasing used employee mobiles, and donating the proceeds to social good, on behalf of organisations. Helping organisation give to meaningful causes that do so much for the community.Many organisations aren't sure what to do with their used mobiles. They either store them in a back room, or have vague, ineffective solutions, such as employee buy-back schemes, or passing on used mobiles to employees.</p>
    <span class="btn">Read More</span>
  </section>
  <section class="benefits">
    <h2 class="section-title">Benefits to Your Organisation</h2>
    <p class="lead">If you are an organisation with a desire to make the world a better place, we can help you.<br>Re-purposing used technology has incredible benefits such as:</p>
    <div class="cards">
      <div class="card"><svg width="22" height="18" viewBox="0 0 22 18" fill="#c5c8a5"><circle cx="11" cy="5" r="4"/><circle cx="4" cy="6" r="3"/><circle cx="18" cy="6" r="3"/><rect x="5" y="10" width="12" height="8" rx="3"/><rect x="0" y="10" width="6" height="6" rx="2"/><rect x="16" y="10" width="6" height="6" rx="2"/></svg><h3>Improve organisational<br>Reputation</h3><p>Individuals and communities have great respect for organisations</p><span class="more">READ MORE</span></div>
      <div class="card"><svg width="18" height="18" viewBox="0 0 18 18" fill="none" stroke="#c5c8a5" stroke-width="2.5"><path d="M3 8a6 6 0 0 1 11-3"/><path d="M15 10a6 6 0 0 1-11 3"/><path d="M14 1v5h-5M4 17v-5h5"/></svg><h3>Provide a simple &amp; effective<br>channel for re-use.</h3><p>We make it easier to clear outdated stock, paving the way for new</p><span class="more">READ MORE</span></div>
      <div class="card"><svg width="20" height="18" viewBox="0 0 20 18"><path d="M2 16C2 6 8 2 19 2c0 10-6 14-14 13z" fill="#c5c8a5"/><path d="M2 16 12 7" stroke="#fff" stroke-width="1.5"/></svg><h3>Environmentally<br>friendly</h3><p>By repurposing used mobiles, for reuse or recycling, extends</p><span class="more">READ MORE</span></div>
      <div class="card"><svg width="20" height="18" viewBox="0 0 20 18"><path d="M1 1h8l10 10-7 7L1 8z" fill="#c5c8a5"/><circle cx="5" cy="5" r="1.6" fill="#fff"/></svg><h3>Offer benefits for<br>your brand</h3><p>Customers are willing to pay premium rates for goods from</p><span class="more">READ MORE</span></div>
      <div class="card"><svg width="20" height="18" viewBox="0 0 20 18" fill="#c5c8a5"><polygon points="10,0 20,5 0,5"/><rect x="2" y="6" width="2.5" height="8"/><rect x="7" y="6" width="2.5" height="8"/><rect x="11" y="6" width="2.5" height="8"/><rect x="15.5" y="6" width="2.5" height="8"/><rect x="0" y="15" width="20" height="3"/></svg><h3>Boost company<br>morale</h3><p>People are happier when working at socially responsible companies</p><span class="more">READ MORE</span></div>
      <div class="card"><svg width="20" height="18" viewBox="0 0 20 18" fill="none" stroke="#c5c8a5" stroke-width="1.8"><path d="M1 1v16h18"/><path d="M4 13l4-5 3 3 6-7"/></svg><h3>Entice millenials</h3><p>They account for the largest percentage of the global workforce and drive trillions of dollars</p><span class="more">READ MORE</span></div>
    </div>
  </section>
  <section class="how">
    <h2 class="section-title">How does it work?</h2>
    <p class="lead">It is simple and easy, with these simple steps</p>
    <div class="step step--top" style="left:89px;top:110px"><b>1</b><p>Contact Velmo Puna directly by calling us, or by completing your details on our form (Click here) and we will contact you.</p></div>
    <div class="step step--bot" style="left:210px;top:109px"><b>2</b><p>Velmo Puna employee can either visit your office to review the stock, or you can send a listing of the mobile model numbers.</p></div>
    <div class="step step--top" style="left:326px;top:95px"><b>3</b><p>Velmo Puna provides you with an estimated valuation, with a listing of the stock.</p></div>
    <div class="step step--bot" style="left:97px;top:231px"><b>4</b><p>Once this is agreed upon, you nominate the charity you would like the money to go towards, or alternatively we pay you directly. This is all agreed in writing.</p></div>
    <div class="step step--top" style="left:217px;top:231px"><b>5</b><p>Payment is made to nominated charity by Velmo Puna, on behalf of you. This is stated to the charity. Alternatively, we pay you directly for the stock.</p></div>
    <div class="step step--bot" style="left:333px;top:222px"><b>6</b><p>Velmo Puna arranges pick-up of the stock. NB: Our employees are young people, mainly students.</p></div>
    <svg class="how-tris" width="90" height="56" viewBox="0 0 90 56"><polygon points="54,0 84,56 24,56" fill="#fff"/><polygon points="28,6 54,56 0,56" fill="#c5c8a5"/></svg>
  </section>
  <section class="contact">
    <h2>Contact Us</h2>
    <p class="lead">Complete the form below and Velmo Puna will contact you.</p>
    <div class="form">
      <div class="field">Organisation Name:</div><div class="field">Address</div>
      <div class="field">Main Contact Name</div><div class="field">Email</div>
      <div class="field field--wide">Phone Number</div>
      <div class="field field--wide">Attachments<svg width="8" height="8" viewBox="0 0 8 8" fill="none" stroke="#888" stroke-width=".8"><path d="M6 3 3 6a1.4 1.4 0 0 1-2-2l3.5-3.5a1 1 0 0 1 1.5 1.5L3 5"/></svg></div>
    </div>
    <span class="btn">Submit</span>
    <div class="contact-photo" role="img" aria-label="Two smiling students with backpacks outside a campus building"></div>
  </section>
  <section class="mission">
    <svg class="mission-photo" width="530" height="246" viewBox="0 0 530 246"><defs><linearGradient id="mg-a" x1="0" y1="0" x2="1" y2="1"><stop offset="0" stop-color="#b9a58a"/><stop offset=".45" stop-color="#9fb2cf"/><stop offset="1" stop-color="#5a4a3c"/></linearGradient></defs><polygon points="465,0 530,0 530,246 268,246 290,205 245,205 378,60" fill="url(#mg-a)" role="img" aria-label="Volunteer doctor examining a smiling child"/></svg>
    <h2>Our Mission</h2>
    <p class="p1">There are thousands of mobiles lying around in offices around Australia. The IT department tend to be at a loss of what to do with them. Most just get taken by the eco-waste collections.</p>
    <p class="p2">Velmo Puna offers a solution to pay for the recycle and give the proceeds to Social Good. Now that back room full of used technology</p>
    <span class="btn">Read More</span>
  </section>
  <footer class="site-footer">
    <div class="social"><span></span><span></span><span></span><span></span></div>
    <nav class="foot-nav"><span>WHAT WE DO</span><span>BENEFITS</span><span>HOW DOES IT WORK?</span><span>CONTACT US</span><span>OUR MISSION</span></nav>
    <p class="copy">© 2020 Velmo Puna . All Rights Reserved &nbsp;|&nbsp; Privacy Policy</p>
  </footer>
</div>

<!-- concept B -->
<div class="page page--b">
  <header class="site-header">
    <div class="brand"><span class="brand-mark"></span>Velmo Puna</div>
    <nav class="nav"><span class="is-active">What we do</span><span>Benefits</span><span>How Does It Work?</span><span>Contact Us</span><span>Our Mission</span></nav>
  </header>
  <section class="hero">
    <div class="hero-photo" role="img" aria-label="Group of young volunteers in matching blue t-shirts in a park"></div>
    <h1 class="hero-title">Velmo Puna helping organisations<br>give to meaningful causes<br>through used technology</h1>
    <span class="btn">Get Started</span>
    <div class="hero-dots"><span></span><span></span><span></span><span></span></div>
    <svg class="corner-tris" width="90" height="70" viewBox="0 0 90 70"><polygon points="30,0 60,52 0,52" fill="#c5c8a5"/><polygon points="62,10 90,66 26,66" fill="#8eafb8"/></svg>
  </section>
  <section class="what">
    <svg class="hex" width="220" height="198" viewBox="0 0 220 198"><polygon points="55,2 165,2 218,99 165,196 55,196 2,99" fill="#fff" stroke="#cfcfcf"/><polygon points="60,6 160,6 210,99 160,192 60,192 10,99" fill="#7d9cb8" role="img" aria-label="Smiling man in glasses and a denim shirt looking at his phone"/></svg>
    <h2>What We Do</h2>
    <p>Velmo Puna creates an easy pathway for organisations, to become more sustainable, renewable and give back to the community. We do this by purchasing used employee mobiles, and donating the proceeds to social good, on behalf of organisations. Helping organisation give to meaningful causes that do so much for the community.Many organisations aren't sure what to do with their used mobiles. They either store them in a back room, or have vague, ineffective solutions, such as employee buy-back schemes, or passing on used mobiles to employees.</p>
    <span class="btn">Read More</span>
  </section>
  <section class="benefits">
    <h2 class="section-title">Benefits to Your Organisation</h2>
    <p class="lead">If you are an organisation with a desire to make the world a better place, we can help you.<br>Re-purposing used technology has incredible benefits such as:</p>
    <div class="cards">
      <div class="card"><svg width="22" height="18" viewBox="0 0 22 18" fill="#c5c8a5"><circle cx="11" cy="5" r="4"/><circle cx="4" cy="6" r="3"/><circle cx="18" cy="6" r="3"/><rect x="5" y="10" width="12" height="8" rx="3"/><rect x="0" y="10" width="6" height="6" rx="2"/><rect x="16" y="10" width="6" height="6" rx="2"/></svg><h3>Improve organisational<br>Reputation</h3><p>Individuals and communities have great respect for organisations</p><span class="more">READ MORE</span></div>
      <div class="card"><svg width="18" height="18" viewBox="0 0 18 18" fill="none" stroke="#c5c8a5" stroke-width="2.5"><path d="M3 8a6 6 0 0 1 11-3"/><path d="M15 10a6 6 0 0 1-11 3"/><path d="M14 1v5h-5M4 17v-5h5"/></svg><h3>Provide a simple &amp; effective<br>channel for re-use.</h3><p>We make it easier to clear outdated stock, paving the way for new</p><span class="more">READ MORE</span></div>
      <div class="card"><svg width="20" height="18" viewBox="0 0 20 18"><path d="M2 16C2 6 8 2 19 2c0 10-6 14-14 13z" fill="#c5c8a5"/><path d="M2 16 12 7" stroke="#fff" stroke-width="1.5"/></svg><h3>Environmentally<br>friendly</h3><p>By repurposing used mobiles, for reuse or recycling, extends</p><span class="more">READ MORE</span></div>
      <div class="card"><svg width="20" height="18" viewBox="0 0 20 18"><path d="M1 1h8l10 10-7 7L1 8z" fill="#c5c8a5"/><circle cx="5" cy="5" r="1.6" fill="#fff"/></svg><h3>Offer benefits for<br>your brand</h3><p>Customers are willing to pay premium rates for goods from</p><span class="more">READ MORE</span></div>
      <div class="card"><svg width="20" height="18" viewBox="0 0 20 18" fill="#c5c8a5"><polygon points="10,0 20,5 0,5"/><rect x="2" y="6" width="2.5" height="8"/><rect x="7" y="6" width="2.5" height="8"/><rect x="11" y="6" width="2.5" height="8"/><rect x="15.5" y="6" width="2.5" height="8"/><rect x="0" y="15" width="20" height="3"/></svg><h3>Boost company<br>morale</h3><p>People are happier when working at socially responsible companies</p><span class="more">READ MORE</span></div>
      <div class="card"><svg width="20" height="18" viewBox="0 0 20 18" fill="none" stroke="#c5c8a5" stroke-width="1.8"><path d="M1 1v16h18"/><path d="M4 13l4-5 3 3 6-7"/></svg><h3>Entice millenials</h3><p>They account for the largest percentage of the global workforce and drive trillions of dollars</p><span class="more">READ MORE</span></div>
    </div>
  </section>
  <section class="how">
    <h2 class="section-title">How does it work?</h2>
    <p class="lead">It is simple and easy, with these simple steps</p>
    <div class="step step--top" style="left:89px;top:110px"><b>1</b><p>Contact Velmo Puna directly by calling us, or by completing your details on our form (Click here) and we will contact you.</p></div>
    <div class="step step--bot" style="left:210px;top:109px"><b>2</b><p>Velmo Puna employee can either visit your office to review the stock, or you can send a listing of the mobile model numbers.</p></div>
    <div class="step step--top" style="left:326px;top:95px"><b>3</b><p>Velmo Puna provides you with an estimated valuation, with a listing of the stock.</p></div>
    <div class="step step--bot" style="left:97px;top:231px"><b>4</b><p>Once this is agreed upon, you nominate the charity you would like the money to go towards, or alternatively we pay you directly. This is all agreed in writing.</p></div>
    <div class="step step--top" style="left:217px;top:231px"><b>5</b><p>Payment is made to nominated charity by Velmo Puna, on behalf of you. This is stated to the charity. Alternatively, we pay you directly for the stock.</p></div>
    <div class="step step--bot" style="left:333px;top:222px"><b>6</b><p>Velmo Puna arranges pick-up of the stock. NB: Our employees are young people, mainly students.</p></div>
    <svg class="how-tris" width="90" height="56" viewBox="0 0 90 56"><polygon points="54,0 84,56 24,56" fill="#fff"/><polygon points="28,6 54,56 0,56" fill="#c5c8a5"/></svg>
  </section>
  <section class="contact">
    <h2>Contact Us</h2>
    <p class="lead">Complete the form below and Velmo Puna will contact you.</p>
    <div class="form">
      <div class="field">Organisation Name:</div><div class="field">Address</div>
      <div class="field">Main Contact Name</div><div class="field">Email</div>
      <div class="field field--wide">Phone Number</div>
      <div class="field field--wide">Attachments<svg width="8" height="8" viewBox="0 0 8 8" fill="none" stroke="#888" stroke-width=".8"><path d="M6 3 3 6a1.4 1.4 0 0 1-2-2l3.5-3.5a1 1 0 0 1 1.5 1.5L3 5"/></svg></div>
    </div>
    <span class="btn">Submit</span>
    <div class="contact-photo" role="img" aria-label="Two smiling students with backpacks outside a campus building"></div>
  </section>
  <section class="mission">
    <svg class="mission-photo" width="530" height="246" viewBox="0 0 530 246"><defs><linearGradient id="mg-b" x1="0" y1="0" x2="1" y2="1"><stop offset="0" stop-color="#b9a58a"/><stop offset=".45" stop-color="#9fb2cf"/><stop offset="1" stop-color="#5a4a3c"/></linearGradient></defs><polygon points="465,0 530,0 530,246 268,246 290,205 245,205 378,60" fill="url(#mg-b)" role="img" aria-label="Volunteer doctor examining a smiling child"/></svg>
    <h2>Our Mission</h2>
    <p class="p1">There are thousands of mobiles lying around in offices around Australia. The IT department tend to be at a loss of what to do with them. Most just get taken by the eco-waste collections.</p>
    <p class="p2">Velmo Puna offers a solution to pay for the recycle and give the proceeds to Social Good. Now that back room full of used technology</p>
    <span class="btn">Read More</span>
  </section>
  <footer class="site-footer">
    <div class="social"><span></span><span></span><span></span><span></span></div>
    <nav class="foot-nav"><span>WHAT WE DO</span><span>BENEFITS</span><span>HOW DOES IT WORK?</span><span>CONTACT US</span><span>OUR MISSION</span></nav>
    <p class="copy">© 2020 Velmo Puna . All Rights Reserved &nbsp;|&nbsp; Privacy Policy</p>
  </footer>
</div>

</body>
</html>
```